Business card for massage therapy company called Brook Fern Wellness

Need business card for massage therapy company called Brook Fern Wellness. Would like my logo on the front and the back of the card I have 3 options of logos and you can play with what looks better.

Would like this information displayed on the back of the card:

Marcus Ellery
Licensed Massage Therapist
321-555-0147
brookfern-example.com
brookfern_rest_

```html
<!DOCTYPE html>
<html lang="en">
<head>
<meta charset="utf-8">
<title>Brook Fern Wellness — Business Card</title>
<link rel="stylesheet" href="https://fonts.googleapis.com/css2?family=Marcellus&display=swap">
<style>
  :root {
    --backdrop: #2b2b2b;
    --sage: #6f7a61;
    --sage-deep: #5d6852;
    --ink: #5f6655;
    --tan: #c4916c;
    --paper: #fbfbf9;
    --white: #ffffff;
  }
  * { box-sizing: border-box; margin: 0; padding: 0; }
  html, body {
    width: 1200px; height: 852px; overflow: hidden;
    background: var(--backdrop);
    font-family: "Marcellus", "Optima", serif;
  }
  .stage {
    position: relative; width: 1200px; height: 852px;
    display: flex; align-items: center; justify-content: center; gap: 56px;
  }
  .card {
    position: relative; width: 520px; height: 300px;
    border-radius: 26px; overflow: hidden;
  }
  /* Front */
  .card--front { background: var(--sage); color: var(--white); }
  .card__pattern {
    position: absolute; inset: 0;
    background: linear-gradient(135deg, var(--sage) 0%, var(--sage-deep) 100%);
    opacity: .35;
  }
  .front-mark {
    position: absolute; left: 50%; top: 112px; transform: translate(-50%, -50%);
    display: flex; align-items: center; gap: 14px;
  }
  .front-mark__dot {
    width: 14px; height: 14px; border-radius: 50%; background: var(--white);
  }
  .front-mark__name { font-size: 30px; letter-spacing: .04em; color: var(--white); }
  .front-links {
    position: absolute; left: 44px; right: 44px; bottom: 34px;
    display: flex; justify-content: space-between; font-size: 15px;
  }
  .front-links__item { display: flex; align-items: center; gap: 8px; }
  .front-links__item svg { width: 15px; height: 15px; }

  /* Back */
  .card--back { background: var(--paper); color: var(--ink); }
  .back-mark {
    position: absolute; left: 34px; top: 118px; width: 210px;
    display: flex; align-items: center; gap: 12px;
  }
  .back-mark__dot {
    flex: none; width: 14px; height: 14px; border-radius: 50%; background: var(--ink);
  }
  .back-mark__name {
    font-size: 24px; line-height: 1.15; letter-spacing: .08em; text-transform: uppercase; color: var(--ink);
  }
  .contact {
    position: absolute; left: 268px; top: 60px;
  }
  .contact__name { font-size: 26px; color: var(--ink); line-height: 1.1; }
  .contact__role { font-size: 14px; color: var(--tan); margin-top: 4px; }
  .contact__list { list-style: none; margin-top: 18px; font-size: 14px; }
  .contact__list li { display: flex; align-items: center; gap: 9px; margin-bottom: 5px; }
  .contact__list svg { width: 12px; height: 12px; flex: none; }
</style>
</head>
<body>
<main class="stage">
  <section class="card card--front" aria-label="Card front">
    <div class="card__pattern" role="img" aria-label="Faint repeating leaf pattern in sage green"></div>
    <div class="front-mark">
      <span class="front-mark__dot"></span>
      <span class="front-mark__name">Brook Fern Wellness</span>
    </div>
    <div class="front-links">
      <span class="front-links__item">
        <svg viewBox="0 0 16 16" fill="none" stroke="#fff" stroke-width="1.3"><circle cx="8" cy="8" r="6.5"/><ellipse cx="8" cy="8" rx="3" ry="6.5"/><line x1="1.5" y1="8" x2="14.5" y2="8"/></svg>
        brookfern-example.com
      </span>
      <span class="front-links__item">
        <svg viewBox="0 0 16 16"><circle cx="8" cy="8" r="3" fill="#fff"/></svg>
        brookfern_rest
      </span>
    </div>
  </section>

  <section class="card card--back" aria-label="Card back">
    <div class="back-mark">
      <span class="back-mark__dot"></span>
      <span class="back-mark__name">Brook Fern Wellness</span>
    </div>
    <div class="contact">
      <h1 class="contact__name">Marcus Ellery</h1>
      <p class="contact__role">Licensed Massage Therapist</p>
      <ul class="contact__list">
        <li><svg viewBox="0 0 16 16"><path d="M4 1.5l2.5 3-1.6 1.6a9 9 0 0 0 5 5l1.6-1.6 3 2.5-1.8 2.5C7 14 2 9 1.5 3.3z" fill="#c4916c"/></svg>321-555-0147</li>
        <li><svg viewBox="0 0 16 16"><rect x="1" y="3" width="14" height="10" fill="#c4916c"/><path d="M1 3l7 5 7-5" fill="none" stroke="#fff" stroke-width="1.2"/></svg>marcus@brookfern-example.com</li>
        <li><svg viewBox="0 0 16 16" fill="none" stroke="#c4916c" stroke-width="1.5"><circle cx="8" cy="8" r="6.5"/><line x1="1.5" y1="8" x2="14.5" y2="8"/></svg>www.brookfern-example.com</li>
        <li><svg viewBox="0 0 16 16"><circle cx="8" cy="8" r="3" fill="#c4916c"/></svg>brookfern_rest_</li>
      </ul>
    </div>
  </section>
</main>
</body>
</html>
```